Drug safety monitoring company requires a new corporate website

We are an outsourcing partner to large and small companies within the pharmaceutical industry. Our current website www.orbanquill.co.uk has not been updated in a long time. We want a new web site that is responsive and modern but with a clearly corporate and professional feel. We want a design based on a 12 column grid system (mobile and desktop version). We want to use a new, modern font (not the standard web fonts) - we will purchase as required. Content can be used as is from the current website. Red and white are the corporate colours, so a palate should be developed to match. We do not need as much red as is in the current website. New icons (preferably in svg format) would be great. We can also purchase new images from PhotoVane (or other) as required. We would prefer submissions in Sketch if possible.

Target Market(s)

Pharmaceutical companies

Number of Pages Required

1 page

Font styles to use
Sans Serif

Colors
ec1f27
ffffff

Requirements
Must have
• Design based on 12 column grid system.
Responsive design (i.e. require a mobile and desktop version).
How should the menu look between desktop and mobile?
A coherent colour palete.
Content to come from the existing website: www.orbanquill.co.uk
How should links be styled?
How should headings, sub-headings, paragraphs be styled?
Nice to have
• Custom developed icons (these are along the bottom of the page on the existing website: Medical Information; Pharmacovigilance; Literature Monitoring; Training).
New imagery (the images on the current website are dated).
Submission ideally as Sketch files (but we are okay with photoshop too).
A new, modern, non-standard font.
Not so much red in the design.
If we had buttons on the website, how should they be styled?
If we had a form on the website, how should the fields be styled?

```html
<!DOCTYPE html>
<html lang="en">
<head>
<meta charset="utf-8">
<title>Orban Quill Pharmacovigilance – Responsive Website</title>
<link href="https://fonts.googleapis.com/css2?family=Montserrat:wght@400;500;600;700&display=swap" rel="stylesheet">
<style>
:root{
  --red:#e4202a;
  --ink:#1f1f22;
  --text:#4a4a4f;
  --dark:#2b2a2e;
  --dark-2:#333236;
  --soft:#f3f3f4;
  --mid:#d5d5d7;
  --line:#cfcfd3;
  --white:#ffffff;
  --blue-1:#cfe0ee;
  --blue-2:#2f5f8f;
}
*{box-sizing:border-box;margin:0;padding:0}
html,body{width:1200px;height:4084px;overflow:hidden;background:var(--white)}
body{position:relative;font-family:"Montserrat",Arial,sans-serif;color:var(--text)}

.board-title{position:absolute;top:56px;font-size:28px;font-weight:700;color:var(--ink);text-align:center}
.board-title.mobile{left:0;width:370px}
.board-title.desktop{left:520px;width:400px}
.accent-rule{position:absolute;left:716px;width:5px;background:var(--red)}

.frame{position:absolute;top:135px;background:var(--white);box-shadow:0 2px 14px rgba(0,0,0,.14);overflow:hidden}
.frame.desktop{left:375px;width:718px;height:2009px}
.frame.mobile{left:77px;width:239px;height:3805px}
section,header.site-head,footer.site-foot{position:relative;overflow:hidden}

.logo{display:inline-flex;align-items:center;gap:5px;font-weight:700;color:var(--red);letter-spacing:.3px}
.logo i{display:block;border-radius:50%;background:var(--red)}
.phone{display:flex;align-items:center;gap:6px}
.phone svg{fill:var(--red);flex:none}
.phone small{display:block;font-size:6px;letter-spacing:1.2px;font-weight:600;color:var(--ink)}
.phone b{display:block;font-size:10px;font-weight:700;color:var(--red)}
.on-dark .phone small{color:#e6e6e6}
.on-dark .phone b{color:#fff}

.btn{display:inline-flex;align-items:center;gap:5px;background:var(--red);color:#fff;font-weight:700;border-radius:20px;text-transform:uppercase;letter-spacing:.3px}
.btn svg{fill:#fff}
.photo{position:absolute}
.hl{color:var(--red)}
p{line-height:1.75}

/* ---------- Desktop ---------- */
.frame.desktop .site-head{height:59px;display:flex;align-items:center;padding:0 67px;justify-content:space-between}
.frame.desktop .site-head .logo{font-size:13px}
.frame.desktop .site-head .logo i{width:9px;height:9px}
.nav{display:flex;gap:11px;font-size:7.5px;font-weight:600;color:var(--ink);margin-left:110px}
.frame.desktop .hero{height:348px;background:var(--dark)}
.frame.desktop .hero .photo{right:0;top:0;width:400px;height:348px;background:radial-gradient(circle at 60% 40%,#e9e6df 0,#c9c3b8 18%,#c02a2e 38%,#3a383b 70%,#2b2a2e 100%)}
.hero-copy{position:absolute;color:#fff}
.frame.desktop .hero-copy{left:67px;top:96px;width:280px}
.frame.desktop .hero-copy h1{font-size:20px;line-height:30px;font-weight:600}
.frame.desktop .hero-copy p{font-size:12px;line-height:18px;margin:8px 0 18px;color:#e8e8e8}
.frame.desktop .btn{font-size:7px;padding:8px 20px}
.hero-copy .hl{border-bottom:2px solid var(--red)}

.frame.desktop .welcome{height:515px}
.welcome h2{font-size:21px;font-weight:600;color:var(--ink);text-align:center;line-height:28px}
.welcome h2 .hl{display:block;font-weight:600}
.frame.desktop .welcome h2{margin-top:32px}
.frame.desktop .intro{width:490px;margin:14px auto 0;font-size:7.6px;text-align:center}
.functions-copy h3,.section-title{font-weight:600;color:var(--ink)}
.frame.desktop .functions-copy{position:absolute;left:67px;top:218px;width:275px}
.frame.desktop .functions-copy h3{font-size:21px;margin-bottom:14px}
.frame.desktop .functions-copy p{font-size:7.6px;margin-bottom:12px}
.collage{position:absolute}
.frame.desktop .collage{left:353px;top:209px;width:290px;height:265px}
.collage .frame-line{position:absolute;border:4px solid var(--red)}
.collage .photo.a{background:linear-gradient(135deg,var(--blue-1),#9dbbd8 55%,#d8782e 80%,var(--blue-2))}
.collage .photo.b{background:linear-gradient(135deg,#3a4d6a,#7da8cf 50%,#d9e7f2)}
.frame.desktop .collage .frame-line{left:80px;top:56px;width:160px;height:165px}
.frame.desktop .collage .photo.a{left:0;top:0;width:208px;height:183px}
.frame.desktop .collage .photo.b{left:124px;top:120px;width:166px;height:145px}

.services{background:var(--soft)}
.frame.desktop .services{height:259px}
.section-title{text-align:center;font-size:21px}
.frame.desktop .services .section-title{padding-top:38px}
.cards{display:flex}
.frame.desktop .cards{gap:14px;margin:20px 0 0 67px}
.card{background:#fff;text-align:center;box-shadow:0 1px 4px rgba(0,0,0,.06)}
.frame.desktop .card{width:135px;height:130px;padding-top:11px}
.card .icon{display:block;margin:0 auto;background:var(--red);border-radius:50%}
.frame.desktop .card .icon{width:46px;height:46px}
.card h4{font-weight:600;color:var(--ink)}
.frame.desktop .card h4{font-size:9px;margin:11px 0 4px}
.card p{line-height:1.6}
.frame.desktop .card p{font-size:6.6px;padding:0 9px}

.brochure{background:var(--mid)}
.frame.desktop .brochure{height:283px}
.brochure .photo{background:linear-gradient(120deg,#f4f4f4 0,#fff 40%,#e9e9ea 55%,#7f96b0 75%,#3b5575)}
.frame.desktop .brochure .photo{left:92px;top:32px;width:254px;height:208px}
.brochure h3{font-weight:600;color:var(--ink)}
.frame.desktop .brochure-copy{position:absolute;left:382px;top:92px}
.frame.desktop .brochure h3{font-size:21px;line-height:29px;margin-bottom:18px}

.frame.desktop .contact{height:296px}
.contact h3{font-weight:600;color:var(--ink)}
.frame.desktop .contact-copy{position:absolute;left:67px;top:48px;width:260px}
.frame.desktop .contact h3{font-size:21px}
.frame.desktop .contact-copy p{font-size:9.6px;line-height:13px;margin:12px 0 10px}
.connect{position:relative;border:1px solid #bdbdc2;display:flex;align-items:center;justify-content:center;gap:4px}
.connect legend{position:absolute;top:-7px;left:50%;transform:translateX(-50%);background:#fff;padding:0 3px;font-size:11px;color:#777}
.connect span{display:block;border-radius:50%;background:#3f4e6f}
.frame.desktop .connect{width:138px;height:48px;margin-top:26px}
.frame.desktop .connect span{width:21px;height:21px}
.form{position:absolute}
.field{border:1px solid #c5c5ca;font-size:8px;color:#555;padding:0 11px;display:flex;align-items:center}
.field em{color:var(--red);font-style:normal}
.frame.desktop .form{left:367px;top:54px;width:284px}
.frame.desktop .form .row{display:flex;gap:13px}
.frame.desktop .field{height:26px;flex:1;margin-bottom:16px}
.frame.desktop .field.message{height:77px;align-items:flex-start;padding-top:9px}
.frame.desktop .form .btn{margin-top:-4px;padding:8px 15px}

.site-foot{background:var(--dark);color:#fff}
.frame.desktop .site-foot{height:249px}
.frame.desktop .foot-brand{position:absolute;left:67px;top:44px}
.site-foot .logo{color:#fff}
.site-foot .logo i{background:var(--red)}
.frame.desktop .site-foot .logo{font-size:14px;margin-bottom:24px}
.frame.desktop .site-foot .logo i{width:10px;height:10px}
.foot-col h5{font-size:8px;font-weight:600;letter-spacing:.3px}
.foot-col ul{list-style:none}
.foot-col li{font-size:7px;text-transform:uppercase}
.frame.desktop .foot-col{position:absolute;top:44px}
.frame.desktop .foot-col h5{margin-bottom:22px}
.frame.desktop .foot-col li{line-height:18px}
.foot-rule{position:absolute;height:1px;background:var(--red)}
.frame.desktop .foot-rule{left:67px;right:67px;top:218px}
.copyright{position:absolute;font-size:7px;text-align:center;color:#e8e8e8}
.frame.desktop .copyright{left:0;right:0;top:227px}

/* ---------- Mobile ---------- */
.frame.mobile .site-head{height:39px;display:flex;align-items:center;justify-content:space-between;padding:0 12px}
.frame.mobile .site-head .logo{font-size:8px}
.frame.mobile .site-head .logo i{width:6px;height:6px}
.burger{width:8px;height:7px;border-top:1.5px solid var(--ink);border-bottom:1.5px solid var(--ink);position:relative}
.burger::after{content:"";position:absolute;left:0;right:0;top:1.5px;border-top:1.5px solid var(--ink)}
.frame.mobile .hero{height:399px;background:var(--dark)}
.frame.mobile .hero-copy{left:0;right:0;top:42px;text-align:center}
.frame.mobile .hero-copy h1{font-size:17px;line-height:25px;font-weight:600}
.frame.mobile .hero-copy p{font-size:10.5px;line-height:14px;margin:6px 24px 16px;color:#e8e8e8}
.frame.mobile .btn{font-size:6px;padding:6px 14px}
.frame.mobile .hero .photo{left:0;right:0;top:183px;height:216px;background:radial-gradient(circle at 55% 55%,#ecebe5 0,#c8c2b6 20%,#c12a2f 42%,#3a383b 72%,#2b2a2e 100%)}

.frame.mobile .welcome{height:937px}
.frame.mobile .welcome h2{font-size:21px;line-height:29px;margin-top:38px}
.frame.mobile .intro{font-size:7.4px;margin:14px 12px 0;text-align:center}
.frame.mobile .functions-copy{text-align:center;margin:42px 12px 0}
.frame.mobile .functions-copy h3{font-size:21px;line-height:28px;margin-bottom:14px}
.frame.mobile .functions-copy p{font-size:7.4px;margin-bottom:12px}
.frame.mobile .collage{left:11px;top:689px;width:218px;height:201px}
.frame.mobile .collage .frame-line{left:58px;top:42px;width:124px;height:126px;border-width:3px}
.frame.mobile .collage .photo.a{left:0;top:0;width:158px;height:140px}
.frame.mobile .collage .photo.b{left:95px;top:91px;width:123px;height:110px}

.frame.mobile .services{height:735px}
.frame.mobile .services .section-title{padding-top:36px}
.frame.mobile .cards{flex-direction:column;align-items:center;gap:23px;margin-top:24px}
.frame.mobile .card{width:133px;height:130px;padding-top:11px}
.frame.mobile .card .icon{width:48px;height:48px}
.frame.mobile .card h4{font-size:9.5px;margin:10px 0 4px}
.frame.mobile .card p{font-size:6.6px;padding:0 9px}

.frame.mobile .brochure{height:392px;text-align:center}
.frame.mobile .brochure .photo{left:27px;top:46px;width:190px;height:163px}
.frame.mobile .brochure-copy{position:absolute;left:0;right:0;top:250px}
.frame.mobile .brochure h3{font-size:19px;line-height:26px;margin-bottom:22px}

.frame.mobile .contact{height:557px;text-align:center}
.frame.mobile .contact h3{font-size:21px;margin-top:30px}
.frame.mobile .contact-copy p{font-size:10px;line-height:13px;margin:12px 24px 10px}
.frame.mobile .contact-copy .phone{justify-content:center}
.frame.mobile .connect{width:138px;height:46px;margin:24px auto 0}
.frame.mobile .connect span{width:21px;height:21px}
.frame.mobile .form{left:12px;right:12px;top:260px}
.frame.mobile .field{height:27px;margin-bottom:15px;font-size:8px}
.frame.mobile .field.message{height:77px;align-items:flex-start;padding-top:9px}
.frame.mobile .form .btn{margin-top:2px;padding:8px 16px}

.frame.mobile .site-foot{height:746px;text-align:center}
.frame.mobile .foot-brand{padding-top:50px;display:flex;flex-direction:column;align-items:center}
.frame.mobile .site-foot .logo{font-size:15px;margin-bottom:22px}
.frame.mobile .site-foot .logo i{width:10px;height:10px}
.frame.mobile .foot-col h5{font-size:8px;margin-bottom:24px}
.frame.mobile .foot-col li{line-height:18px}
.frame.mobile .foot-col.quick{margin-top:52px}
.frame.mobile .foot-col.serv{margin-top:50px}
.frame.mobile .foot-col.other{margin-top:52px}
.frame.mobile .foot-rule{left:12px;right:12px;top:692px}
.frame.mobile .copyright{left:10px;right:10px;top:703px;line-height:11px}
</style>
</head>
<body>

<svg width="0" height="0" style="position:absolute" aria-hidden="true">
  <defs>
    <symbol id="i-phone" viewBox="0 0 24 24"><path d="M6.6 2.5c.6-.3 1.3-.1 1.6.5l2 3.6c.3.5.2 1.2-.3 1.6l-1.6 1.3c1 2.2 2.8 4 5 5l1.3-1.6c.4-.5 1.1-.6 1.6-.3l3.6 2c.6.3.8 1 .5 1.6l-1.1 2.4c-.4.8-1.3 1.3-2.2 1.1C10 18.6 5.4 14 4.3 7.9c-.2-.9.3-1.8 1.1-2.2z"/></symbol>
    <symbol id="i-send" viewBox="0 0 24 24"><path d="M2 11l20-9-9 20-2-9z"/></symbol>
    <symbol id="i-doc" viewBox="0 0 48 48"><rect x="15" y="11" width="18" height="24" rx="2" fill="none" stroke="#fff" stroke-width="2"/><path d="M19 18h10M19 22h10M19 26h7" stroke="#fff" stroke-width="2"/></symbol>
    <symbol id="i-pill" viewBox="0 0 48 48"><rect x="14" y="12" width="14" height="22" rx="3" fill="none" stroke="#fff" stroke-width="2"/><path d="M14 18h14" stroke="#fff" stroke-width="2"/><rect x="24" y="26" width="12" height="7" rx="3.5" fill="none" stroke="#fff" stroke-width="2" transform="rotate(-30 30 29)"/></symbol>
    <symbol id="i-monitor" viewBox="0 0 48 48"><rect x="12" y="13" width="24" height="16" rx="1.5" fill="none" stroke="#fff" stroke-width="2"/><path d="M20 34h8M24 29v5" stroke="#fff" stroke-width="2"/><circle cx="23" cy="21" r="4" fill="none" stroke="#fff" stroke-width="2"/><path d="M26 24l4 4" stroke="#fff" stroke-width="2"/></symbol>
    <symbol id="i-train" viewBox="0 0 48 48"><rect x="22" y="12" width="15" height="12" fill="none" stroke="#fff" stroke-width="2"/><circle cx="16" cy="17" r="3" fill="none" stroke="#fff" stroke-width="2"/><path d="M11 35v-8c0-2 2-4 5-4s5 2 5 4v8M20 26l4-3" stroke="#fff" stroke-width="2"/></symbol>
  </defs>
</svg>

<h2 class="board-title mobile">Mobile View</h2>
<h2 class="board-title desktop">Desktop View</h2>

<!-- ================= DESKTOP ================= -->
<main class="frame desktop">
  <header class="site-head">
    <span class="logo"><i></i>Orban Quill</span>
    <nav class="nav"><span>HOME</span><span>ABOUT US</span><span>QPPV</span><span>OUR SERVICES</span><span>CONTACT US</span><span>CLIENT</span></nav>
    <div class="phone"><svg width="20" height="20"><use href="#i-phone"/></svg><div><small>CALL US TODAY!</small><b>0330 2468 135</b></div></div>
  </header>

  <section class="hero">
    <div class="photo" role="img" aria-label="Red, white and yellow capsules spilling from a white pill bottle on a dark surface"></div>
    <div class="hero-copy">
      <h1>At <span class="hl">Orban Quill</span> We Ensure That Your Business</h1>
      <p>has the best Pharmacovigilance support in the industry</p>
      <span class="btn">Contact us</span>
    </div>
  </section>

  <section class="welcome">
    <h2>Welcome to The <span class="hl">Orban Quill Pharmacovigilance</span></h2>
    <p class="intro">We are an outsourcing partner to large and small companies within the pharmaceutical industry. Our range of services is tailored to suit each of our client's needs and cover both human and veterinary medicinal products. Pharmacovigilance is defined by WHO as 'The science and activities relating to the detection, assessment, understanding and prevention of adverse effects or any other drug-related problems'. The process is one of managing risk associated with medicinal products, in an effort to promote their safe and effective use by prescribers and patients.</p>
    <div class="functions-copy">
      <h3>Our Primary Functions</h3>
      <p>are EU QPPV and related pharmacovigilance services to assist and support Marketing Authorisation Holders (MAH), of pharmaceutical product licences, in their efforts to remain compliant with EU regulatory requirements (Regulation 1235/2010 and Directive 2010/84/EU) the deadline for which implementing ended on 21 July 2012.</p>
      <p>The regulatory environment is an ever-changing and evolving one. Legislation is global and the management of this process is complex, requiring a strong relationship between Marketing Authorisation Holders and their QPPV. Good Pharmacovigilance Practice is dependant on a sound understanding of the key principles of this science and the ability to apply this knowledge competently on behalf of the client.</p>
    </div>
    <div class="collage">
      <div class="frame-line"></div>
      <div class="photo a" role="img" aria-label="Orange and white capsules on a pale blue surface beside a blue bottle cap"></div>
      <div class="photo b" role="img" aria-label="Hand touching a network of glowing gear symbols on a blue background"></div>
    </div>
  </section>

  <section class="services">
    <h2 class="section-title">Our Services</h2>
    <div class="cards">
      <article class="card"><svg class="icon"><use href="#i-doc"/></svg><h4>Medical Information</h4><p>Professional enquiry handling to support the safe and effective use of your products</p></article>
      <article class="card"><svg class="icon"><use href="#i-pill"/></svg><h4>Pharmacovigilance</h4><p>Ease the regulatory burden and keep compliant with current pharmacovigilance legislation.</p></article>
      <article class="card"><svg class="icon"><use href="#i-monitor"/></svg><h4>Literature Monitoring</h4><p>Product safety through surveillance of published articles and case reports.</p></article>
      <article class="card"><svg class="icon"><use href="#i-train"/></svg><h4>Training</h4><p>Professional enquiry handling to support the safe and effective use of your products</p></article>
    </div>
  </section>

  <section class="brochure">
    <div class="photo" role="img" aria-label="Open bi-fold company brochure mockup with a stethoscope photo on the cover"></div>
    <div class="brochure-copy">
      <h3>Download Our<br>Company Brochure</h3>
      <span class="btn">Learn more</span>
    </div>
  </section>

  <section class="contact">
    <div class="contact-copy">
      <h3>Contact Us</h3>
      <p>If you got any questions, please do not hesitate to send us a message. Say Hi!</p>
      <div class="phone"><svg width="20" height="20"><use href="#i-phone"/></svg><div><small>CALL US TODAY!</small><b>0330 2468 135</b></div></div>
      <div class="connect"><legend>Connect Us</legend><span></span><span></span><span></span><span></span></div>
    </div>
    <form class="form">
      <div class="row"><div class="field">Enter Name <em>&nbsp;*</em></div><div class="field">Mobile No <em>&nbsp;*</em></div></div>
      <div class="field">Enter Email <em>&nbsp;*</em></div>
      <div class="field message">Message <em>&nbsp;*</em></div>
      <span class="btn"><svg width="8" height="8"><use href="#i-send"/></svg>Submit now</span>
    </form>
  </section>

  <footer class="site-foot on-dark">
    <div class="foot-brand">
      <span class="logo"><i></i>Orban Quill</span>
      <div class="phone"><svg width="18" height="18"><use href="#i-phone"/></svg><div><small>CALL US TODAY!</small><b>0330 2468 135</b></div></div>
    </div>
    <div class="foot-col" style="left:257px"><h5>QUICK LINK</h5><ul><li>Home</li><li>About us</li><li>QPPV</li><li>Our services</li><li>Contact us</li><li>Client</li></ul></div>
    <div class="foot-col" style="left:384px"><h5>SERVICES</h5><ul><li>Medical information</li><li>Pharmacovigilance</li><li>Literature monitoring</li><li>Training</li></ul></div>
    <div class="foot-col" style="left:557px"><h5>OTHERS</h5><ul><li>Terms &amp; conditions</li><li>Privacy policy</li><li>News</li><li>FAQ</li><li>Log in</li></ul></div>
    <div class="foot-rule"></div>
    <p class="copyright">Copyright © 2020 Orban Quill Ltd (Registered in England &amp; Wales : 08126473)</p>
  </footer>
</main>

<!-- ================= MOBILE ================= -->
<main class="frame mobile">
  <header class="site-head">
    <span class="logo"><i></i>Orban Quill</span>
    <span class="burger"></span>
  </header>

  <section class="hero">
    <div class="hero-copy">
      <h1>At <span class="hl">Orban Quill</span> We Ensure That Your Business</h1>
      <p>has the best Pharmacovigilance support in the industry</p>
      <span class="btn">Contact us</span>
    </div>
    <div class="photo" role="img" aria-label="Red, white and yellow capsules spilling from a white pill bottle on a dark surface"></div>
  </section>

  <section class="welcome">
    <h2>Welcome to<br>The <span class="hl">Orban Quill Pharmacovigilance</span></h2>
    <p class="intro">We are an outsourcing partner to large and small companies within the pharmaceutical industry. Our range of services is tailored to suit each of our client's needs and cover both human and veterinary medicinal products. Pharmacovigilance is defined by WHO as 'The science and activities relating to the detection, assessment, understanding and prevention of adverse effects or any other drug-related problems'. The process is one of managing risk associated with medicinal products, in an effort to promote their safe and effective use by prescribers and patients.</p>
    <div class="functions-copy">
      <h3>Our Primary<br>Functions</h3>
      <p>are EU QPPV and related pharmacovigilance services to assist and support Marketing Authorisation Holders (MAH), of pharmaceutical product licences, in their efforts to remain compliant with EU regulatory requirements (Regulation 1235/2010 and Directive 2010/84/EU) the deadline for which implementing ended on 21 July 2012.</p>
      <p>The regulatory environment is an ever-changing and evolving one. Legislation is global and the management of this process is complex, requiring a strong relationship between Marketing Authorisation Holders and their QPPV. Good Pharmacovigilance Practice is dependant on a sound understanding of the key principles of this science and the ability to apply this knowledge competently on behalf of the client.</p>
    </div>
    <div class="collage">
      <div class="frame-line"></div>
      <div class="photo a" role="img" aria-label="Orange and white capsules on a pale blue surface beside a blue bottle cap"></div>
      <div class="photo b" role="img" aria-label="Hand touching a network of glowing gear symbols on a blue background"></div>
    </div>
  </section>

  <section class="services">
    <h2 class="section-title">Our Services</h2>
    <div class="cards">
      <article class="card"><svg class="icon"><use href="#i-doc"/></svg><h4>Medical Information</h4><p>Professional enquiry handling to support the safe and effective use of your products</p></article>
      <article class="card"><svg class="icon"><use href="#i-pill"/></svg><h4>Pharmacovigilance</h4><p>Ease the regulatory burden and keep compliant with current pharmacovigilance legislation.</p></article>
      <article class="card"><svg class="icon"><use href="#i-monitor"/></svg><h4>Literature Monitoring</h4><p>Product safety through surveillance of published articles and case reports.</p></article>
      <article class="card"><svg class="icon"><use href="#i-train"/></svg><h4>Training</h4><p>Professional enquiry handling to support the safe and effective use of your products</p></article>
    </div>
  </section>

  <section class="brochure">
    <div class="photo" role="img" aria-label="Open bi-fold company brochure mockup with a stethoscope photo on the cover"></div>
    <div class="brochure-copy">
      <h3>Download Our<br>Company Brochure</h3>
      <span class="btn">Learn more</span>
    </div>
  </section>

  <section class="contact">
    <div class="contact-copy">
      <h3>Contact Us</h3>
      <p>If you got any questions, please do not hesitate to send us a message.</p>
      <div class="phone"><svg width="20" height="20"><use href="#i-phone"/></svg><div style="text-align:left"><small>CALL US TODAY!</small><b>0330 2468 135</b></div></div>
      <div class="connect"><legend>Connect Us</legend><span></span><span></span><span></span><span></span></div>
    </div>
    <form class="form">
      <div class="field">Enter Name <em>&nbsp;*</em></div>
      <div class="field">Mobile No <em>&nbsp;*</em></div>
      <div class="field">Enter Email <em>&nbsp;*</em></div>
      <div class="field message">Message <em>&nbsp;*</em></div>
      <span class="btn"><svg width="8" height="8"><use href="#i-send"/></svg>Submit now</span>
    </form>
  </section>

  <footer class="site-foot on-dark">
    <div class="foot-brand">
      <span class="logo"><i></i>Orban Quill</span>
      <div class="phone"><svg width="18" height="18"><use href="#i-phone"/></svg><div style="text-align:left"><small>CALL US TODAY!</small><b>0330 2468 135</b></div></div>
    </div>
    <div class="foot-col quick"><h5>QUICK LINK</h5><ul><li>Home</li><li>About us</li><li>QPPV</li><li>Our services</li><li>Contact us</li><li>Client</li></ul></div>
    <div class="foot-col serv"><h5>SERVICES</h5><ul><li>Medical information</li><li>Pharmacovigilance</li><li>Literature monitoring</li><li>Training</li></ul></div>
    <div class="foot-col other"><h5>OTHERS</h5><ul><li>Terms &amp; conditions</li><li>Privacy policy</li><li>News</li><li>FAQ</li><li>Log in</li></ul></div>
    <div class="foot-rule"></div>
    <p class="copyright">Copyright © 2020 Orban Quill Ltd<br>(Registered in England &amp; Wales : 08126473)</p>
  </footer>
</main>

<div class="accent-rule" style="top:2286px;height:477px"></div>
<div class="accent-rule" style="top:2913px;height:477px"></div>

</body>
</html>
```